Business Card for a new businees.

need a very good business for a new company based in Riverside California call Levy Lantern LLC. We help client file taxes, resolve tax debt and attain peace of mind We help people nationwide solve Tax problems. We help with Installment agreements, Offers in Compromise, Partial Pay Installment Agreements, Currently Not Collectible status, Liens and Levy Removal, Garnishment removal. We offer individualized services

Target Market(s)

Any one with Tax Problems nationwide. My clients span across age, occupation etc

Contact Information for Business Card

Card must be attractive and have enough information to let client know we care and call us

Colors

Designer to choose colors to be used in the design.

Requirements
Must have
• the basics and then surprise me
Nice to have
• surprise m

```html
<!DOCTYPE html>
<html lang="en">
<head>
<meta charset="utf-8">
<title>Levy Lantern LLC — Business Card</title>
<link href="https://fonts.googleapis.com/css2?family=Roboto:wght@400;500;700&display=swap" rel="stylesheet">
<style>
  :root {
    --backdrop: #d9d6d2;
    --card: #1b1b1b;
    --card-edge: #111111;
    --gold: #f2c81e;
    --gold-deep: #c9a21a;
    --ink-light: #f4f4f4;
  }
  * { margin: 0; padding: 0; box-sizing: border-box; }
  html, body {
    width: 1200px; height: 716px; overflow: hidden;
    background: var(--backdrop);
    font-family: "Roboto", Arial, sans-serif;
  }
  .canvas {
    position: relative; width: 1200px; height: 716px;
    display: flex; align-items: center; justify-content: center; gap: 48px;
  }
  .card {
    position: relative; width: 540px; height: 309px;
    background: var(--card);
    border: 1px solid var(--card-edge);
    box-shadow: 0 10px 28px rgba(0,0,0,.25);
    overflow: hidden;
  }
  /* Front */
  .card-front {
    display: flex; flex-direction: column; align-items: center; justify-content: center; gap: 26px;
  }
  .brand-name {
    color: var(--gold); font-weight: 700; font-size: 38px; letter-spacing: .5px;
  }
  .front-web { color: var(--gold); font-size: 19px; letter-spacing: .4px; }

  /* Back */
  .person { position: absolute; left: 44px; top: 40px; }
  .person-name { color: var(--gold); font-weight: 700; font-size: 18px; }
  .person-title { color: var(--gold-deep); font-weight: 500; font-size: 16px; margin-top: 2px; }
  .address {
    position: absolute; left: 44px; top: 112px;
    color: var(--ink-light); font-size: 15px; line-height: 20px;
  }
  .contacts {
    position: absolute; left: 44px; top: 170px; list-style: none;
    color: var(--ink-light); font-size: 15px; line-height: 20px;
  }
  .contacts li { display: flex; align-items: center; gap: 8px; }
  .contacts svg { width: 12px; height: 12px; fill: var(--gold); flex: none; }
  .rule-long {
    position: absolute; left: 0; top: 250px; width: 340px; height: 3px; background: var(--gold);
  }
  .back-web {
    position: absolute; left: 350px; top: 238px;
    color: var(--ink-light); font-size: 17px; letter-spacing: .3px;
  }
  .rule-short {
    position: absolute; right: 0; top: 280px; width: 56px; height: 3px; background: var(--gold);
  }
  .back-brand {
    position: absolute; right: 30px; top: 118px;
    display: flex; align-items: center; gap: 10px;
  }
  .brand-mark { width: 16px; height: 16px; background: var(--gold); border-radius: 50%; }
  .back-brand .brand-name { font-size: 26px; }
</style>
</head>
<body>
  <main class="canvas">
    <section class="card card-front" aria-label="Card front">
      <div class="brand-name">Levy Lantern LLC</div>
      <div class="front-web">www.levylantern.com</div>
    </section>

    <section class="card card-back" aria-label="Card back">
      <div class="person">
        <div class="person-name">Employee Name</div>
        <div class="person-title">Title</div>
      </div>
      <address class="address" style="font-style:normal">
        4620 Arlington Ave. Ste 310<br>Riverside, CA 92504
      </address>
      <ul class="contacts">
        <li><svg viewBox="0 0 12 12"><path d="M2.5 0.5 L4.5 0.5 L5.2 3.3 L3.8 4.4 Q5 7 7.6 8.2 L8.7 6.8 L11.5 7.5 L11.5 9.5 Q11.5 11.5 9.5 11.5 Q0.5 11 0.5 2.5 Q0.5 0.5 2.5 0.5Z"/></svg>951-555-0148</li>
        <li><svg viewBox="0 0 12 12"><path d="M3 0 H9 Q10 0 10 1 V11 Q10 12 9 12 H3 Q2 12 2 11 V1 Q2 0 3 0Z M3.2 1.5 V9.5 H8.8 V1.5Z"/></svg>951-555-0148</li>
        <li><svg viewBox="0 0 12 12"><path d="M0 2 H12 V10 H0Z M1 3 L6 6.8 L11 3 V2.8 H1Z" fill-rule="evenodd"/></svg>info@levylantern.com</li>
      </ul>
      <div class="back-brand">
        <span class="brand-mark"></span>
        <span class="brand-name">Levy Lantern LLC</span>
      </div>
      <div class="rule-long"></div>
      <div class="back-web">www.levylantern.com</div>
      <div class="rule-short"></div>
    </section>
  </main>
</body>
</html>
```